We need a book cover design for a fitness professional's guidebook to be a successful trainer. LA celebrity trainer offers 7 ideas that are designed to transform any fitness professional's career and life. The cover design we are into is attached an includes the image of a man who is half dressed in a business suit and half dressed in fitness gear. The back photo should demonstrate the four sphere's the book is designed around (also attached) and will be included on the back with a brief description of the material (included below) and a short bio and photo of the writer (attached) at the very bottom. We'd like the book to have a work book feel, or text book geometry to it. The brand colors are Black and Red. The final design should invoke the feeling of success, health and happiness.

Dimensions: 8 5/8 x 5 3/4

USE WEBSITE AS REFERENCE FOR BRAND COLORS AND DESIGNS:
BrenoVigor.net

BOOK TITLE:
RISING STRIDE
"A fitness professional's guidebook to be a successful trainer."

BACK COVER COPY:
Celebrity conditioning specialist and trainer consultant, Tavo Minardi, offers powerful ideas that are designed to transform every fitness professional's career and life. Reveal essential tools that every trainer and entrepreneur should know. Discover the deeper meaning of yourself and your career by working smarter rather than harder.

Find out how to create a brand, advertise it, and hone in on your market. Create buzz by landing magazine press. How to build celebrity clientele. Explore the world of multi-media projects. And finally, what to do when you reach your goals. This is an opportunity for trainer's to capture a share of the fitness industry’s vast $27B market. Fulfill your fullest earning potential while also understanding what the true meaning of success is, and how to achieve it. Learn what you love to do, what you do well, what the fitness industry needs and what it will pay for.

Aimed at the trainers who want to know the mistakes to avoid, and the habits to establish that will set them apart from the rest, Rising Stride is THE guidebook that has the power to take your career and life in the direction that will prepare you for continued success. Use these business ideas to promote your passive income, generate multiple streams of revenue and increase your investments, resulting in more freedom and access in the fitness industry and beyond. Let Rising Stride unleash your potential to be a successful trainer.

BACK AUTHOR BIO:
Los Angeles based celebrity trainer and trainer consultant, Tavo Minardi, CSCS, developed his very own “Ember” technique and fitness brand. Minardi’s clients include a mix of celebrities, professional athletes, musicians, fashion models, students, political figures and corporate professionals. Kelvo magazine described Minardi’s fitness DVD, TAVOMOVE, as “a workout you’ll look forward to”. Tavo was also the co-developer of a natural energy drink that increases energy and metabolism with an ancient Peruvian super food. Additionally backed by his finance and advertising education, Tavo has consulted several trainers and fitness brands to guide them to their maximum earning potential.

Target Market(s)

Fitness Industry/Trainers

Industry/Entity Type

Advertising

Requirements
Must have
• Consistent with website logo colors, shapes and fonts.

```html
<!DOCTYPE html>
<html lang="en">
<head>
<meta charset="utf-8">
<title>Rising Stride – Book Cover</title>
<link href="https://fonts.googleapis.com/css2?family=Playfair+Display:wght@400;700&family=Questrial&family=Oswald:wght@300;400&family=Montserrat:wght@400;600&display=swap" rel="stylesheet">
<style>
  :root{
    --red:#e8473f;
    --red-deep:#d93a33;
    --orange:#f39a3a;
    --black:#0d0d0d;
    --white:#ffffff;
    --ink:#1a1a1a;
    --photo-dark:#2f4b60;
    --photo-light:#8fb3c9;
  }
  *{margin:0;padding:0;box-sizing:border-box}
  html,body{width:1200px;height:867px;overflow:hidden;background:#fff}
  .cover{position:relative;width:1200px;height:867px;overflow:hidden}

  /* Back cover */
  .back{position:absolute;left:0;top:0;width:567px;height:867px;background:var(--red);color:var(--white)}
  .back-title{position:absolute;top:62px;left:0;width:567px;text-align:center;
    font-family:"Playfair Display",serif;font-size:40px;font-weight:400;letter-spacing:1px}
  .back-copy{position:absolute;top:138px;left:53px;width:476px;
    font-family:"Questrial",sans-serif;font-size:12.4px;line-height:1.36;text-align:left}
  .back-copy p{margin-bottom:17px}
  .bio{position:absolute;top:563px;left:53px;width:514px;height:176px;background:var(--black)}
  .bio-photo{position:absolute;left:10px;top:8px;width:125px;height:155px;
    background:linear-gradient(160deg,#8a8a8a,#3c3c3c)}
  .bio-text{position:absolute;left:150px;top:6px;width:352px;
    font-family:"Montserrat",sans-serif;font-size:8.9px;line-height:1.42;color:var(--white)}
  .back-url{position:absolute;bottom:32px;left:0;width:567px;text-align:center;
    font-family:"Questrial",sans-serif;font-size:15px;letter-spacing:2px}

  /* Spine */
  .spine{position:absolute;left:567px;top:0;width:61px;height:867px;background:var(--black)}
  .spine-title,.spine-author{position:absolute;left:50%;white-space:nowrap;
    transform-origin:center;transform:translate(-50%,-50%) rotate(90deg)}
  .spine-title{top:300px;font-family:"Playfair Display",serif;font-size:34px;color:var(--white)}
  .spine-title .accent{color:var(--red)}
  .spine-author{top:668px;font-family:"Oswald",sans-serif;font-weight:300;font-size:22px;letter-spacing:3px;color:var(--white)}

  /* Front cover */
  .front{position:absolute;left:628px;top:0;width:572px;height:867px;background:var(--white)}
  .front-photo{position:absolute;left:0;top:0;width:572px;height:400px;
    background:linear-gradient(120deg,var(--photo-dark) 0%,#5f7f95 45%,var(--photo-light) 100%)}
  .swoosh{position:absolute;left:0;top:230px;width:572px;height:190px}
  .front-title{position:absolute;left:0;width:572px;text-align:center;
    font-family:"Playfair Display",serif;font-weight:400;line-height:1}
  .title-top{top:408px;font-size:92px;letter-spacing:9px;color:var(--ink)}
  .title-bottom{top:508px;font-size:100px;letter-spacing:7px;color:var(--red)}
  .subtitle{position:absolute;left:0;width:572px;text-align:center;color:var(--ink)}
  .subtitle-lead{top:632px;font-family:"Questrial",sans-serif;font-size:21px;letter-spacing:.5px}
  .subtitle-strong{top:664px;font-family:"Montserrat",sans-serif;font-weight:600;font-size:24px;letter-spacing:.5px}
  .rule{position:absolute;left:90px;top:708px;width:392px;height:2px;background:var(--red)}
  .author-band{position:absolute;left:0;top:778px;width:572px;height:89px;background:var(--red);
    display:flex;align-items:center;justify-content:center}
  .author-name{font-family:"Oswald",sans-serif;font-weight:300;font-size:42px;letter-spacing:5px;color:var(--white)}
</style>
</head>
<body>
<div class="cover">

  <section class="back">
    <h2 class="back-title">RISING STRIDE</h2>
    <div class="back-copy">
      <p>Celebrity conditioning specialist and trainer consultant, Tavo Minardi, offers powerful ideas that are designed to transform every fitness professional's career and life. Reveal essential tools that every trainer and entrepreneur should know. Discover the deeper meaning of yourself and your career by working smarter rather than harder.</p>
      <p>Find out how to create a brand, advertise it, and hone in on your market. Create buzz by landing magazine press. How to build celebrity clientele. Explore the world of multi-media projects. And finally, what to do when you reach your goals. This is an opportunity for trainer's to capture a share of the fitness industry’s vast $27B market. Fulfill your fullest earning potential while also understanding what the true meaning of success is, and how to achieve it. Learn what you love to do, what you do well, what the fitness industry needs and what it will pay for.</p>
      <p>Aimed at the trainers who want to know the mistakes to avoid, and the habits to establish that will set them apart from the rest, Rising Stride is THE guidebook that has the power to take your career and life in the direction that will prepare you for continued success. Use these business ideas to promote your passive income, generate multiple streams of revenue and increase your investments, resulting in more freedom and access in the fitness industry and beyond. Let Rising Stride unleash your potential to be a successful trainer.</p>
    </div>
    <div class="bio">
      <div class="bio-photo" role="img" aria-label="Portrait photo of the author seated on a rooftop"></div>
      <p class="bio-text">Los Angeles based celebrity trainer and trainer consultant, Tavo Minardi, CSCS, developed his very own “Ember” technique and fitness brand. Minardi’s clients include a mix of celebrities, professional athletes, musicians, fashion models, students, political figures and corporate professionals. Kelvo magazine described Minardi’s fitness DVD, TAVOMOVE, as “a workout you’ll look forward to”. Tavo was also the co-developer of a natural energy drink that increases energy and metabolism with an ancient Peruvian super food. Additionally backed by his finance and advertising education, Tavo has consulted several trainers and fitness brands to guide them to their maximum earning potential.</p>
    </div>
    <p class="back-url">www.brenovigor.net</p>
  </section>

  <section class="spine">
    <span class="spine-title">RISING <span class="accent">STRIDE</span></span>
    <span class="spine-author">TAVO MINARDI</span>
  </section>

  <section class="front">
    <div class="front-photo" role="img" aria-label="Photo of a man and woman lifting dumbbells in a gym"></div>
    <svg class="swoosh" viewBox="0 0 572 190" preserveAspectRatio="none" aria-hidden="true">
      <path d="M0 40 C150 60 300 120 572 50 L572 190 L0 190 Z" fill="var(--orange)"/>
      <path d="M0 70 C160 95 320 145 572 80 L572 190 L0 190 Z" fill="var(--white)"/>
      <path d="M0 95 C170 125 330 160 572 108 L572 120 C330 175 170 140 0 110 Z" fill="var(--red)"/>
      <path d="M0 125 C200 150 360 175 572 125 L572 190 L0 190 Z" fill="var(--white)"/>
    </svg>
    <h1 class="front-title title-top">RISING</h1>
    <h1 class="front-title title-bottom">STRIDE</h1>
    <p class="subtitle subtitle-lead">A FITNESS PROFESSIONAL’S GUIDEBOOK</p>
    <p class="subtitle subtitle-strong">TO BE A SUCCESSFUL TRAINER</p>
    <div class="rule"></div>
    <div class="author-band"><span class="author-name">TAVO MINARDI</span></div>
  </section>

</div>
</body>
</html>
```